Glow Jam - Concert Poster

We need a poster for a concert involving 3 bands. Marvolin, Auntie's Pickles and Velvet Hank. The event is called the Glow Jam. The poster will be a take away. We plan to print some to give out and some for advertising. Should be something people will want to put up on a wall. The poster should have a psychedelic "flavor", colorful.
Info. that needs to be on the poster: Glow Jam - Band Names - Bartleby's Sound Lodge - 4183 Route 12, Cedar Hollow OR - $10 advance Tix - $12 at Door - for tickets www.bartlebyssound. - 21 and Over - March 21 2015 - Doors open at 7:00.

```html
<!DOCTYPE html>
<html lang="en">
<head>
<meta charset="utf-8">
<title>Glow Jam – Concert Poster</title>
<link rel="stylesheet" href="https://fonts.googleapis.com/css2?family=Oswald:wght@600;700&family=Righteous&family=Syncopate:wght@700&display=swap">
<style>
  :root {
    --sun: #ffc20e;
    --orange: #f7941d;
    --magenta: #ec2fb5;
    --pink: #f06bc8;
    --purple: #6a2c8f;
    --teal: #1fb58f;
    --white: #ffffff;
  }
  * { margin: 0; padding: 0; box-sizing: border-box; }
  html, body { width: 848px; height: 1200px; overflow: hidden; background: var(--sun); }
  .poster {
    position: relative;
    width: 848px;
    height: 1200px;
    overflow: hidden;
    background: var(--sun);
  }
  .event-title {
    position: absolute;
    top: 30px;
    left: 0;
    width: 848px;
    text-align: center;
    font-family: "Syncopate", sans-serif;
    font-weight: 700;
    font-size: 108px;
    letter-spacing: -3px;
    line-height: 1;
    color: var(--magenta);
    text-shadow: -2px 2px 0 var(--purple), -4px 4px 0 var(--purple), -6px 6px 0 var(--purple);
  }
  .event-date {
    position: absolute;
    top: 160px;
    left: 64px;
    font-family: "Oswald", sans-serif;
    font-weight: 700;
    color: var(--purple);
    font-size: 54px;
    line-height: 1;
    letter-spacing: -1px;
  }
  .event-date sup { font-size: 24px; vertical-align: 24px; }
  .event-year {
    position: absolute;
    top: 208px;
    left: 194px;
    font-family: "Oswald", sans-serif;
    font-weight: 600;
    font-size: 18px;
    line-height: 1;
    color: var(--magenta);
  }
  .doors {
    position: absolute;
    top: 166px;
    right: 58px;
    font-family: "Oswald", sans-serif;
    font-weight: 700;
    font-size: 17px;
    line-height: 1;
    color: var(--purple);
  }
  .illustration {
    position: absolute;
    top: 230px;
    left: 0;
    width: 848px;
    height: 720px;
    background:
      radial-gradient(ellipse 28% 38% at 50% 52%, var(--pink) 0%, var(--teal) 70%, rgba(31,181,143,0) 100%),
      radial-gradient(ellipse 60% 45% at 50% 38%, var(--orange) 0%, rgba(247,148,29,0.5) 55%, rgba(255,194,14,0) 100%);
  }
  .stage {
    position: absolute;
    left: 0;
    top: 820px;
    width: 848px;
    height: 380px;
  }
  .lineup {
    position: absolute;
    top: 982px;
    left: 0;
    width: 848px;
    text-align: center;
    font-family: "Righteous", sans-serif;
    font-size: 48px;
    line-height: 46px;
    letter-spacing: 2px;
    color: var(--sun);
    text-transform: uppercase;
  }
  .venue {
    position: absolute;
    top: 1118px;
    left: 0;
    width: 848px;
    text-align: center;
    font-family: "Oswald", sans-serif;
    color: var(--white);
    text-transform: uppercase;
  }
  .venue-line { font-size: 19px; font-weight: 700; line-height: 24px; }
  .venue-line .address { font-weight: 600; font-size: 18px; }
  .ticket-line { font-size: 13px; font-weight: 600; letter-spacing: 0.3px; line-height: 20px; }
  .ticket-line span { margin: 0 10px; }
  .age-badge {
    position: absolute;
    top: 1110px;
    left: 754px;
    width: 44px;
    height: 44px;
    border-radius: 50%;
    background: var(--white);
    color: var(--magenta);
    font-family: "Oswald", sans-serif;
    font-weight: 700;
    font-size: 18px;
    line-height: 44px;
    text-align: center;
  }
</style>
</head>
<body>
<main class="poster">
  <h1 class="event-title">GLOW JAM</h1>
  <p class="event-date">MARCH 21<sup>ST</sup></p>
  <p class="event-year">2015</p>
  <p class="doors">DOORS OPEN AT 7:00</p>

  <div class="illustration" role="img" aria-label="Psychedelic illustration: a pink-haired woman eating a melting ice cream cone under orange clouds, with an arrow, a moon, chains, a goldfish, a bird, a peace sign and a second woman's portrait, melting into pink paint"></div>

  <svg class="stage" viewBox="0 0 848 380" aria-hidden="true">
    <path d="M0 60 C120 30 200 90 300 70 C380 55 470 40 560 70 C660 100 760 40 848 70 L848 380 L0 380 Z" fill="var(--magenta)"/>
    <path d="M190 80 C260 60 320 110 424 95 C520 80 580 60 660 100 L700 380 L150 380 Z" fill="var(--purple)"/>
  </svg>

  <div class="lineup">
    <p>Marvolin</p>
    <p>Auntie's Pickles</p>
    <p>Velvet Hank</p>
  </div>

  <div class="venue">
    <p class="venue-line">Bartleby's Sound Lodge <span class="address">4183 Route 12, Cedar Hollow OR</span></p>
    <p class="ticket-line"><span>$10 Advance Tix</span><span>$12 at Door</span><span>For Tickets: www.bartlebyssound.</span></p>
  </div>

  <div class="age-badge">21+</div>
</main>
</body>
</html>
```